Executive recruiting firm in need of business card design

Executive recruiting firm looking for a sleek, classy and modern business card design; card itself will be square shape, rounded edges and soft touch paper, our colors are dark blues in the navy color scale, silvers and grays. Reference our website for a better idea of our company's feel and goals at Staffbrook.com - our company message is "Employee Engagement Begins at Recruitment" this should be on the card

Industry/Entity Type

Business

```html
<!DOCTYPE html>
<html lang="en">
<head>
<meta charset="utf-8">
<title>Staffbrook Business Card</title>
<link href="https://fonts.googleapis.com/css2?family=Open+Sans:wght@300;400;700&display=swap" rel="stylesheet">
<style>
  :root {
    --navy: #15194a;
    --white: #ffffff;
    --paper: #f4f4f5;
    --silver: #8a8c94;
    --ink-gray: #6b6d75;
    --backdrop: #d9dadd;
  }
  html, body {
    margin: 0;
    padding: 0;
    width: 1200px;
    height: 904px;
    overflow: hidden;
    background: var(--backdrop);
    font-family: "Open Sans", Arial, sans-serif;
  }
  .stage {
    position: relative;
    width: 1200px;
    height: 904px;
  }
  .card {
    position: absolute;
    top: 232px;
    width: 440px;
    height: 440px;
    border-radius: 36px;
    overflow: hidden;
    box-shadow: 0 10px 30px rgba(20, 22, 40, 0.18);
  }
  .card--back {
    left: 120px;
    background: var(--navy);
    color: var(--white);
  }
  .card--front {
    left: 640px;
    background: linear-gradient(135deg, var(--white) 0%, var(--paper) 100%);
    color: var(--navy);
  }
  .brand-name {
    position: absolute;
    margin: 0;
    font-weight: 300;
    letter-spacing: 4px;
    text-transform: uppercase;
    white-space: nowrap;
  }
  .card--back .brand-name {
    left: 0;
    right: 0;
    top: 158px;
    text-align: center;
    font-size: 30px;
    color: var(--white);
  }
  .tagline {
    position: absolute;
    left: 0;
    right: 0;
    bottom: 52px;
    margin: 0;
    text-align: center;
    font-size: 14px;
    font-weight: 400;
    letter-spacing: 0.3px;
    color: var(--white);
  }
  .card--front .brand-name {
    left: 82px;
    top: 86px;
    font-size: 34px;
    color: var(--navy);
  }
  .edge-tab {
    position: absolute;
    left: 0;
    top: 218px;
    width: 26px;
    height: 44px;
    background: var(--navy);
  }
  .person {
    position: absolute;
    left: 82px;
    top: 214px;
  }
  .person__name {
    margin: 0;
    font-size: 19px;
    font-weight: 700;
    color: var(--navy);
  }
  .person__role {
    margin: 2px 0 0 14px;
    font-size: 14px;
    color: var(--ink-gray);
  }
  .contacts {
    position: absolute;
    left: 82px;
    top: 300px;
    margin: 0;
    padding: 0;
    list-style: none;
  }
  .contacts__item {
    display: flex;
    align-items: center;
    gap: 12px;
    margin-bottom: 6px;
    font-size: 14px;
    color: var(--ink-gray);
  }
  .contacts__icon {
    width: 16px;
    height: 16px;
    flex: none;
  }
</style>
</head>
<body>
<main class="stage">
  <section class="card card--back" aria-label="Card back">
    <p class="brand-name">Staffbrook</p>
    <p class="tagline">Employee Engagement Begins at Recruitment</p>
  </section>

  <section class="card card--front" aria-label="Card front">
    <p class="brand-name">Staffbrook</p>
    <span class="edge-tab"></span>
    <div class="person">
      <p class="person__name">John Smith</p>
      <p class="person__role">Manager</p>
    </div>
    <ul class="contacts">
      <li class="contacts__item">
        <svg class="contacts__icon" viewBox="0 0 16 16" aria-hidden="true">
          <circle cx="8" cy="8" r="8" fill="var(--navy)"/>
          <path d="M5.2 4.2l1.4 1.6-.7 1c.5 1.1 1.2 1.8 2.3 2.3l1-.7 1.6 1.4-.9 1.2C7.4 10.8 5.2 8.6 4.4 5.1z" fill="#fff"/>
        </svg>
        +999 9999 9999
      </li>
      <li class="contacts__item">
        <svg class="contacts__icon" viewBox="0 0 16 16" aria-hidden="true">
          <circle cx="8" cy="8" r="8" fill="var(--navy)"/>
          <rect x="4" y="5.2" width="8" height="5.6" fill="#fff"/>
          <path d="M4 5.2l4 3 4-3" fill="none" stroke="var(--navy)" stroke-width="0.9"/>
        </svg>
        info@mywebsite.com
      </li>
      <li class="contacts__item">
        <svg class="contacts__icon" viewBox="0 0 16 16" aria-hidden="true">
          <circle cx="8" cy="8" r="8" fill="var(--navy)"/>
          <circle cx="8" cy="8" r="4" fill="none" stroke="#fff" stroke-width="1"/>
          <ellipse cx="8" cy="8" rx="1.6" ry="4" fill="none" stroke="#fff" stroke-width="0.9"/>
          <line x1="4" y1="8" x2="12" y2="8" stroke="#fff" stroke-width="0.9"/>
        </svg>
        www.mywebsite.com
      </li>
    </ul>
  </section>
</main>
</body>
</html>
```